Business IT Services Billboard to attract local small businesses

We are Brivolane, a premier Managed Service Provider (MSP) specializing in comprehensive IT services and VOIP phone solutions exclusively for businesses. Our goal is to create a dynamic and visually engaging billboard advertisement that not only highlights our cutting-edge IT solutions but also emphasizes our state-of-the-art VOIP phone services. This billboard should communicate our commitment to providing innovative, reliable, and holistic technology solutions.
Target Market(s)
small business
Industry/Entity Type
Information Technology
Colors
Designer to choose colors to be used in the design.
Look and feel
Each slider illustrates characteristics of the customer's brand and the style your logo design should communicate.

```html
<!DOCTYPE html>
<html lang="en">
<head>
<meta charset="utf-8">
<title>Brivolane – Seamless Technology Billboard</title>
<link rel="stylesheet" href="https://fonts.googleapis.com/css2?family=Orbitron:wght@700;900&family=Montserrat:wght@300;500;600;700&display=swap">
<style>
  :root {
    --brand-blue: #1b75bb;
    --brand-blue-deep: #155f9c;
    --map-light: #d4ecf4;
    --map-mid: #a9d8ea;
    --map-deep: #7fbfdc;
    --voip-tint: #dcebf4;
    --white: #ffffff;
    --rule-grey: #e6e7e9;
    --pill-ring: #c9dcef;
  }
  * { margin: 0; padding: 0; box-sizing: border-box; }
  html, body {
    width: 1200px; height: 696px; overflow: hidden;
    background: var(--white);
  }
  .billboard {
    position: relative;
    width: 1200px; height: 696px;
    overflow: hidden;
    background: var(--white);
    font-family: "Montserrat", sans-serif;
  }
  .billboard__shape { position: absolute; inset: 0; }
  .brand-name {
    position: absolute; left: 56px; top: 100px;
    font-weight: 700; font-size: 38px; line-height: 1;
    color: var(--brand-blue);
    display: flex; align-items: center; gap: 10px;
  }
  .brand-name__mark {
    width: 20px; height: 20px; border-radius: 50%;
    background: var(--brand-blue);
  }
  .hero-art {
    position: absolute; left: 20px; top: 182px;
    width: 520px; height: 356px;
    border-radius: 14px;
    background: linear-gradient(135deg, var(--map-light) 0%, var(--map-mid) 55%, var(--map-deep) 100%);
  }
  .service-label {
    position: absolute; left: 173px; top: 552px; width: 200px;
    text-align: center;
    font-weight: 300; font-size: 46px; line-height: 1;
    color: var(--voip-tint);
    letter-spacing: 1px;
  }
  .headline { position: absolute; left: 0; top: 0; }
  .headline text { font-family: "Orbitron", sans-serif; font-weight: 900; fill: var(--white); }
  .headline .headline__sub { font-family: "Montserrat", sans-serif; font-weight: 600; }
  .tagline {
    position: absolute; left: 600px; top: 310px; width: 520px;
    text-align: center; color: var(--white);
    font-weight: 500; font-size: 19.5px; line-height: 24px;
  }
  .cta-pill {
    position: absolute; left: 744px; top: 488px;
    width: 229px; height: 64px;
    background: var(--white);
    border-radius: 32px 26px 0 0;
  }
  .cta-pill__icon {
    position: absolute; left: -6px; top: -8px;
    width: 74px; height: 74px; border-radius: 50%;
    background: var(--white);
    border: 4px solid var(--pill-ring);
    display: flex; align-items: center; justify-content: center;
  }
  .cta-pill__text {
    position: absolute; left: 78px; top: 14px;
    color: var(--brand-blue); line-height: 1;
  }
  .cta-pill__title { font-family: "Orbitron", sans-serif; font-weight: 900; font-size: 17px; letter-spacing: 0.4px; }
  .cta-pill__sub { font-weight: 700; font-size: 9.5px; margin-top: 3px; letter-spacing: 0.3px; }
  .web-address {
    position: absolute; left: 620px; top: 562px; width: 480px;
    text-align: center; color: var(--white);
    font-weight: 600; font-size: 33px; letter-spacing: 0.5px;
  }
</style>
</head>
<body>
<main class="billboard">
  <svg class="billboard__shape" width="1200" height="696" viewBox="0 0 1200 696">
    <defs>
      <radialGradient id="network-glow" cx="85%" cy="60%" r="60%">
        <stop offset="0" stop-color="#2a8bd0" stop-opacity="0.55"/>
        <stop offset="1" stop-color="#1b75bb" stop-opacity="0"/>
      </radialGradient>
    </defs>
    <polygon points="646,0 1200,0 1200,696 0,696" fill="var(--brand-blue)"/>
    <polygon points="646,0 1200,0 1200,696 0,696" fill="url(#network-glow)" role="img" aria-label="Faint network of connected nodes across the blue field"/>
  </svg>

  <div class="brand-name"><span class="brand-name__mark"></span>Brivolane</div>

  <div class="hero-art" role="img" aria-label="World map with call routes and a smartphone showing an incoming VOIP call"></div>
  <div class="service-label">VOIP</div>

  <svg class="headline" width="1200" height="300" viewBox="0 0 1200 300">
    <text x="668" y="158" font-size="50" textLength="381" lengthAdjust="spacingAndGlyphs">SEAMLESS</text>
    <text x="615" y="219" font-size="50" textLength="488" lengthAdjust="spacingAndGlyphs">TECHNOLOGY</text>
    <text class="headline__sub" x="611" y="257" font-size="22" textLength="494" lengthAdjust="spacingAndGlyphs">SOLUTIONS FOR MODERN BUSINESSES</text>
    <rect x="587" y="263" width="541" height="2" fill="var(--rule-grey)"/>
    <rect x="587" y="269" width="541" height="13" fill="var(--rule-grey)"/>
  </svg>

  <p class="tagline">Innovative IT and VOIP Solutions Tailored<br>For Your Business Success</p>

  <div class="cta-pill">
    <div class="cta-pill__icon">
      <svg width="36" height="36" viewBox="0 0 36 36" fill="none" stroke="var(--brand-blue)" stroke-width="2.2">
        <circle cx="18" cy="18" r="15"/>
        <ellipse cx="18" cy="18" rx="6.5" ry="15"/>
        <line x1="3" y1="18" x2="33" y2="18"/>
        <path d="M6 10 H30 M6 26 H30"/>
      </svg>
    </div>
    <div class="cta-pill__text">
      <div class="cta-pill__title">TRANSFORM</div>
      <div class="cta-pill__sub">YOUR TECH TODAY AT</div>
    </div>
  </div>

  <div class="web-address">WWW.BRIVOLANE.COM</div>
</main>
</body>
</html>
```